brightquokka.net we need a webpage designed for our new product

We need a webpage designed for our new range of products from our new brand. We have had a logo designed on sketchharbor (see attached) and we want to keep to this theme. Our first product is a range of affordable app controlled LED lightbulbs.

I have added some photos that we think is good inspirational material and would be good as a background to this website, but we want the site to look modern but not conventional. We would like something that makes our company look quirky not corporate.

Thats it

Target Market(s)

Our product is being stocked by big name online retailers in the UK, the page will get link through hits from our app. Our target market is gadget freaks of all ages.

Industry/Entity Type

It Company

Requirements
Must have
• We are going to need a help page, text to be uploaded next few days.

We need a contact page.

design my work on iOS and Android as most people will access page through their handset or tablet.
Should not have
• We do not want anything too corporate.

```html
<!DOCTYPE html>
<html lang="en">
<head>
<meta charset="utf-8">
<title>Bright Quokka – App Controlled LED Light Bulbs</title>
<link href="https://fonts.googleapis.com/css2?family=Open+Sans:wght@300;400;600;700&display=swap" rel="stylesheet">
<style>
:root{
  --green:#3fae3a;
  --green-dark:#2e8f2b;
  --green-light:#5fc45a;
  --charcoal:#3b3b3b;
  --grey:#7b7b7b;
  --grey-tile:#8e8e8e;
  --text:#555;
  --muted:#999;
  --line:#e3e3e3;
  --white:#fff;
  --orange:#e8782a;
}
*{box-sizing:border-box;margin:0;padding:0}
html,body{width:802px;height:1200px;overflow:hidden}
body{font-family:"Open Sans",Arial,sans-serif;color:var(--text);background:var(--white);position:relative}
.wrap{width:650px;margin:0 auto;position:relative}
.inner{width:506px;margin:0 auto;position:relative}

/* header */
.site-header{height:100px;position:relative}
.brand{position:absolute;left:0;top:38px;display:flex;align-items:center;gap:8px}
.brand-dot{width:22px;height:22px;border-radius:50%;background:var(--green)}
.brand-name{font-size:17px;font-weight:700;color:var(--green);letter-spacing:.3px}
.account{position:absolute;right:0;top:10px;display:flex;gap:4px}
.account a{font-size:8px;color:var(--white);background:var(--charcoal);padding:2px 7px;text-decoration:none}
.follow{position:absolute;right:0;top:32px;text-align:right}
.follow span{display:block;font-size:7px;color:var(--muted);margin-bottom:3px}
.social{display:flex;gap:3px;justify-content:flex-end}
.social i{width:13px;height:13px;background:var(--charcoal);display:block}
.social i:nth-child(2){background:var(--grey)}
.social i:nth-child(3){background:#c4473a}
.social i:nth-child(4){background:var(--green)}
.search{position:absolute;right:0;top:56px;width:92px;height:13px;border:1px solid var(--line);font-size:6px;color:var(--muted);padding:2px 4px}

/* nav */
.main-nav{background:var(--green);height:24px;display:flex;border-bottom:2px solid var(--green-dark)}
.main-nav a{flex:1;text-align:center;color:var(--white);font-size:9px;line-height:22px;text-decoration:none;border-right:1px solid var(--green-light)}
.main-nav a:last-child{border-right:0}

/* hero mosaic */
.hero{height:386px;margin-top:10px;position:relative}
.tile{position:absolute;overflow:hidden}
.t-a{left:0;top:0;width:150px;height:190px;background:linear-gradient(160deg,#f4c07a,#c85f1c 70%,#5a2a10)}
.t-b{left:150px;top:0;width:176px;height:130px;background:linear-gradient(135deg,#f3dfc0,#c9a06d 60%,#7a5a3a)}
.t-c{left:326px;top:0;width:180px;height:200px;background:linear-gradient(150deg,#2a3a2c,#4a8a45 55%,#172018)}
.t-f{left:150px;top:130px;width:176px;height:60px;background:linear-gradient(90deg,#2a2a2a,#8a6a40 60%,#e6c892)}
.t-d{left:0;top:190px;width:214px;height:196px;background:linear-gradient(160deg,#3d3a34,#b88b4a 50%,#1d1b18)}
.t-g{left:214px;top:190px;width:56px;height:98px;background:var(--grey-tile)}
.t-h{left:214px;top:288px;width:56px;height:98px;background:#6f6f6f}
.t-i{left:270px;top:190px;width:56px;height:196px;background:linear-gradient(180deg,#d8d4cc,#8d8880)}
.t-j{left:326px;top:200px;width:180px;height:186px;background:linear-gradient(160deg,#e7e7e7,#9c9c9c 60%,#5a5a5a)}
.cap{position:absolute;font-size:8px;color:var(--white);padding:4px 6px}
.cap-orange{left:0;right:0;bottom:0;background:var(--orange)}
.cap-dark{left:0;right:0;top:0;background:rgba(0,0,0,.55)}
.cap-green-tag{right:6px;top:8px;background:var(--green);font-size:9px;font-weight:600;padding:3px 8px}
.cap-bottom{left:0;right:0;bottom:0;background:rgba(0,0,0,.6);font-size:8px}
.cap-green-bar{left:0;right:0;bottom:0;background:var(--green);font-size:11px;padding:6px 8px}
.cap-j{left:0;right:0;bottom:0;background:rgba(30,30,30,.8);font-size:8px;line-height:1.35}
.cap-j small{display:block;font-size:6px;color:#ccc;margin-top:3px}
.icon-tile{display:flex;flex-direction:column;align-items:center;justify-content:center;gap:6px;color:var(--white);font-size:7px}
.cap-i{left:0;right:0;bottom:0;background:rgba(0,0,0,.55);font-size:6px}

/* welcome */
.welcome{margin-top:22px;height:110px;display:flex;gap:14px}
.welcome-badge{width:22px;height:22px;border-radius:50%;background:var(--green);flex:none;display:flex;align-items:center;justify-content:center}
.welcome-body{flex:1}
.welcome h1{font-size:13px;font-weight:600;color:#333;margin-bottom:6px}
.welcome p{font-size:7px;line-height:1.55;color:var(--muted);margin-bottom:7px}
.welcome p a{color:var(--green);text-decoration:none}
.welcome-photo{width:96px;height:100px;background:linear-gradient(180deg,#f6e2b8,#b98a4a 55%,#3b2c1c);flex:none}

/* featured */
.featured{margin-top:22px;height:200px;position:relative;display:flex}
.featured-copy{width:253px;background:var(--green);color:var(--white);padding:22px 22px}
.featured h2{font-size:25px;font-weight:300;margin-bottom:10px}
.featured p{font-size:7px;line-height:1.55;margin-bottom:6px}
.btn-more{display:inline-block;margin-top:8px;border:1px solid var(--white);color:var(--white);font-size:8px;padding:5px 12px;text-decoration:none}
.featured-photo{flex:1;background:radial-gradient(circle at 55% 45%,#fdfdf6,#dcdcd4 35%,#8f8f8a 75%)}
.slide-arrow{position:absolute;top:88px;width:14px;height:24px;background:var(--charcoal);display:flex;align-items:center;justify-content:center}
.slide-arrow.prev{left:-14px}
.slide-arrow.next{right:-14px}
.dots{position:absolute;right:14px;bottom:8px;display:flex;gap:4px}
.dots i{width:6px;height:6px;border-radius:50%;background:#bbb;display:block}
.dots i:first-child{background:var(--green)}

/* footer band */
.footer-band{position:absolute;left:0;right:0;top:915px;height:50px;background:var(--charcoal)}
.footer-band .wrap{height:50px;display:flex;align-items:center;justify-content:space-between}
.footer-band h3{color:var(--white);font-size:15px;font-weight:400}
.follow-here{display:flex;align-items:center;gap:8px}
.follow-here span{color:var(--white);font-size:17px;font-weight:300;margin-right:4px}
.follow-here i{width:15px;height:15px;border:1px solid #ccc;border-radius:50%;display:block}

/* footer cols */
.footer-cols{position:absolute;left:0;right:0;top:978px}
.footer-cols .wrap{display:flex;gap:22px}
.fcol{flex:1}
.fcol h4{color:var(--green);font-size:8px;font-weight:700;margin-bottom:6px;text-transform:uppercase}
.fcol p{font-size:6.5px;line-height:1.6;color:var(--muted)}
.fcol ul{list-style:none}
.fcol li{font-size:6.5px;color:var(--muted);border:1px solid var(--line);padding:2px 4px;margin-bottom:4px}
.legal{position:absolute;left:0;right:0;bottom:0;height:18px;background:var(--green);color:var(--white);font-size:6.5px;text-align:center;line-height:18px}
</style>
</head>
<body>

<header class="site-header wrap">
  <div class="brand"><span class="brand-dot"></span><span class="brand-name">brightquokka.net</span></div>
  <div class="account"><a href="#">Login</a><a href="#">Join</a></div>
  <div class="follow"><span>FOLLOW US ON</span>
    <div class="social"><i></i><i></i><i></i><i></i></div>
  </div>
  <div class="search">Search</div>
</header>

<nav class="main-nav wrap">
  <a href="#">Home</a><a href="#">About us</a><a href="#">Services</a><a href="#">Products</a><a href="#">Blog</a><a href="#">Contact</a>
</nav>

<section class="hero inner">
  <div class="tile t-a" role="img" aria-label="Photo of warm orange glowing bulbs">
    <div class="cap cap-orange">Lorem ipsum dolor sit amet consectetur</div>
  </div>
  <div class="tile t-b" role="img" aria-label="Photo of a hand holding a light bulb">
    <div class="cap cap-dark">Lorem ipsum dolor sit amet consectetuer</div>
  </div>
  <div class="tile t-c" role="img" aria-label="Photo of a green lit room controlled by app">
    <div class="cap cap-green-tag">App Controlled Lights</div>
    <div class="cap cap-bottom">A legacy of Innovation</div>
  </div>
  <div class="tile t-f" role="img" aria-label="Photo of a lamp in a living room"></div>
  <div class="tile t-d" role="img" aria-label="Photo of hanging filament bulbs">
    <div class="cap cap-green-bar">&laquo; Lorem ipsum dolor sit amet</div>
  </div>
  <div class="tile t-g icon-tile">
    <svg width="22" height="22" viewBox="0 0 22 22" fill="none" stroke="#fff" stroke-width="1.6"><path d="M3 7l8-4 8 4-8 4z"/><path d="M3 11l8 4 8-4"/><path d="M3 15l8 4 8-4"/></svg>
    <span>Application</span>
  </div>
  <div class="tile t-h icon-tile">
    <svg width="22" height="22" viewBox="0 0 22 22" fill="none" stroke="#fff" stroke-width="1.6"><circle cx="8" cy="9" r="5"/><circle cx="14" cy="9" r="5"/><circle cx="11" cy="14" r="5"/></svg>
    <span>Different Colours</span>
  </div>
  <div class="tile t-i" role="img" aria-label="Photo of a bulb on a shelf">
    <div class="cap cap-i">Lorem ipsum dolor sit amet</div>
  </div>
  <div class="tile t-j" role="img" aria-label="Photo of a smart bulb beside a phone">
    <div class="cap cap-j">Lorem Ipsum Dolor Sit Amet Colour Volume adjusting<small>Lorem ipsum dolor sit amet, consectetur adipiscing elit sed do eiusmod &nbsp;» Read the full blog</small></div>
  </div>
</section>

<section class="welcome inner">
  <div class="welcome-badge">
    <svg width="10" height="10" viewBox="0 0 10 10"><path d="M2 5l2 2 4-4" stroke="#fff" stroke-width="1.6" fill="none"/></svg>
  </div>
  <div class="welcome-body">
    <h1>Welcome to Bright Quokka</h1>
    <p>Lorem Ipsum is simply dummy text of the printing and typesetting industry. Lorem Ipsum has been the industry's standard dummy text ever since the 1500s, when an unknown printer took a galley of type and scrambled it to make a type specimen book. It has survived not only five centuries, but also the leap into electronic typesetting, remaining essentially unchanged.</p>
    <p>Lorem Ipsum is simply dummy text of the printing and typesetting industry. Lorem Ipsum has been the industry's standard dummy text ever since the 1500s, when an unknown printer took a galley of type and scrambled it to make a type specimen book. It has survived not only five centuries, but also the leap into electronic typesetting, remaining essentially unchanged. <a href="#">Read more</a></p>
  </div>
  <div class="welcome-photo" role="img" aria-label="Photo of a glowing table lamp"></div>
</section>

<section class="featured inner">
  <div class="featured-copy">
    <h2>Featured Services</h2>
    <p>Lorem ipsum dolor sit amet, consectetuer adipiscing elit, sed diam nonummy nibh euismod tincidunt ut laoreet dolore magna aliquam erat volutpat. Ut wisi enim ad minim veniam, quis nostrud exerci tation ullamcorper suscipit lobortis nisl ut aliquip ex ea commodo consequat.</p>
    <p>Ut wisi enim ad minim veniam, quis nostrud exerci tation ullamcorper suscipit lobortis nisl ut aliquip ex ea commodo.</p>
    <a class="btn-more" href="#">VIEW MORE</a>
  </div>
  <div class="featured-photo" role="img" aria-label="Photo of a bright LED light bulb"></div>
  <span class="slide-arrow prev"><svg width="6" height="10" viewBox="0 0 6 10"><path d="M5 1L1 5l4 4" stroke="#fff" stroke-width="1.5" fill="none"/></svg></span>
  <span class="slide-arrow next"><svg width="6" height="10" viewBox="0 0 6 10"><path d="M1 1l4 4-4 4" stroke="#fff" stroke-width="1.5" fill="none"/></svg></span>
  <div class="dots"><i></i><i></i><i></i></div>
</section>

<section class="footer-band">
  <div class="wrap">
    <h3>App Controled LED Light Bulbs</h3>
    <div class="follow-here"><span>Follow Us Here</span><i></i><i></i><i></i><i></i><i></i></div>
  </div>
</section>

<footer class="footer-cols">
  <div class="wrap">
    <div class="fcol">
      <h4>About us</h4>
      <p>Lorem ipsum dolor sit amet, consectetur adipiscing elit, sed do eiusmod tempor incididunt ut labore et dolore magna aliqua. Ut enim ad minim veniam, quis nostrud exercitation ullamco laboris nisi ut aliquip ex ea commodo consequat.</p>
    </div>
    <div class="fcol">
      <h4>Suggestions</h4>
      <ul><li>Your name</li><li>Your email</li><li>Subject</li><li>Message</li><li>Send</li></ul>
    </div>
    <div class="fcol">
      <h4>Help &amp; Support</h4>
      <p>Lorem ipsum dolor sit amet, consectetur adipiscing elit, sed do eiusmod tempor incididunt ut labore et dolore magna aliqua. Ut enim ad minim veniam, quis nostrud exercitation ullamco.</p>
    </div>
    <div class="fcol">
      <h4>Contact us</h4>
      <p>Bright Quokka<br>12 Lantern Row,<br>Fenwick,<br>FN4 2QL</p>
    </div>
  </div>
</footer>

<div class="legal">Copyright 2014 Bright Quokka</div>

</body>
</html>
```